Beacon Guard Services

Our Company is a security business which needs a cut edge design, the final product should have all relevant information and maintain a bold but modern and professional look.

Target Market(s)

A cut edge design which will attract any audience

Industry/Entity Type

Security

Contact Information for Business Card

BEACON GUARD SERVICES

Daniel Hofstra
Operations Manager
Phone: 0412 739 215

Email: info@beaconguard.com.au
Web: www.beaconguard.com.au

Requirements
Must have
• Must be double sided and contain all relevant information and the company logo.

```html
<!DOCTYPE html>
<html lang="en">
<head>
<meta charset="utf-8">
<title>Beacon Guard Services – Business Card</title>
<link rel="stylesheet" href="https://fonts.googleapis.com/css2?family=Michroma&display=swap">
<style>
  :root {
    --slate: #566e77;
    --slate-dark: #445a62;
    --slate-light: #6a818a;
    --orange: #f39c1f;
    --white: #ffffff;
    --paper: #f4f6f7;
    --ink: #4b626b;
    --stage: #e6e8ea;
  }
  * { margin: 0; padding: 0; box-sizing: border-box; }
  html, body {
    width: 1200px; height: 900px; overflow: hidden;
    background: var(--stage);
    font-family: "Michroma", sans-serif;
  }
  .canvas {
    width: 1200px; height: 900px;
    display: flex; flex-direction: column;
    align-items: center; justify-content: center; gap: 56px;
  }
  .card {
    position: relative;
    width: 600px; height: 366px;
    overflow: hidden;
    box-shadow: 0 10px 30px rgba(0,0,0,.18);
  }

  /* Back side */
  .card-back {
    background: linear-gradient(135deg, var(--slate-light) 0%, var(--slate) 55%, var(--slate-dark) 100%);
  }
  .card-back .brand {
    position: absolute; left: 0; right: 0; top: 130px;
    display: flex; align-items: center; justify-content: center; gap: 16px;
  }
  .card-back .brand-mark {
    width: 22px; height: 22px; background: var(--white);
  }
  .card-back .brand-name {
    color: var(--white); font-size: 34px; letter-spacing: 1px;
  }
  .card-back .brand-sub {
    position: absolute; left: 0; right: 0; top: 186px;
    text-align: center; color: var(--white);
    font-size: 12px; letter-spacing: 8px;
  }
  .card-back .web {
    position: absolute; left: 0; right: 0; bottom: 40px;
    text-align: center; color: var(--orange);
    font-size: 13px; letter-spacing: 4px;
  }

  /* Front side */
  .card-front { background: var(--slate); }
  .card-front .top-panel {
    position: absolute; left: 0; top: 0; width: 100%; height: 166px;
    background: linear-gradient(180deg, var(--white) 0%, var(--paper) 100%);
  }
  .card-front .accent {
    position: absolute; left: 0; top: 166px; width: 100%; height: 44px;
  }
  .card-front .brand {
    position: absolute; left: 40px; top: 58px;
    display: flex; align-items: center; gap: 18px;
  }
  .card-front .brand-mark {
    width: 46px; height: 46px; background: var(--ink);
  }
  .card-front .brand-name {
    color: var(--ink); font-size: 30px; letter-spacing: 1px; line-height: 1;
  }
  .card-front .brand-sub {
    color: var(--orange); font-size: 11px; letter-spacing: 7px; margin-top: 8px;
  }
  .person {
    position: absolute; left: 40px; top: 232px;
  }
  .person .name {
    color: var(--orange); font-size: 18px; letter-spacing: .5px;
  }
  .person .role {
    color: var(--white); font-size: 10px; letter-spacing: 1px; margin-top: 10px;
  }
  .contacts {
    position: absolute; left: 320px; top: 206px;
    list-style: none; color: var(--white);
    font-size: 10.5px; letter-spacing: .5px;
  }
  .contacts li {
    display: flex; align-items: center; gap: 12px; height: 24px;
  }
  .contacts svg { width: 13px; height: 13px; flex: none; }
</style>
</head>
<body>
<main class="canvas">

  <section class="card card-back" aria-label="Business card, back">
    <div class="brand">
      <span class="brand-mark"></span>
      <span class="brand-name">BEACON GUARD</span>
    </div>
    <div class="brand-sub">SERVICES</div>
    <div class="web">WWW.BEACONGUARD.COM.AU</div>
  </section>

  <section class="card card-front" aria-label="Business card, front">
    <div class="top-panel"></div>
    <svg class="accent" viewBox="0 0 600 44" preserveAspectRatio="none" aria-hidden="true">
      <polygon points="0,0 600,0 600,8 118,8 106,22 94,8 0,8" fill="var(--orange)"/>
    </svg>
    <div class="brand">
      <span class="brand-mark"></span>
      <div>
        <div class="brand-name">BEACON GUARD</div>
        <div class="brand-sub">SERVICES</div>
      </div>
    </div>

    <div class="person">
      <div class="name">DANIEL HOFSTRA</div>
      <div class="role">OPERATIONS MANAGER</div>
    </div>

    <ul class="contacts">
      <li>
        <svg viewBox="0 0 14 14" aria-hidden="true"><rect x="1" y="1" width="12" height="12" rx="2" fill="var(--orange)"/><path d="M4.5 3.5h2l.6 2-1.2.8a5 5 0 0 0 2.8 2.8l.8-1.2 2 .6v2A1 1 0 0 1 10.5 11 7.5 7.5 0 0 1 3.5 4a1 1 0 0 1 1-.5z" fill="var(--slate)"/></svg>
        <span>0412 739 215</span>
      </li>
      <li>
        <svg viewBox="0 0 14 14" aria-hidden="true"><rect x="1" y="3" width="12" height="8" rx="1" fill="var(--orange)"/><path d="M1.5 3.5 7 8l5.5-4.5" fill="none" stroke="var(--slate)" stroke-width="1"/></svg>
        <span>INFO@BEACONGUARD.COM.AU</span>
      </li>
      <li>
        <svg viewBox="0 0 14 14" aria-hidden="true"><circle cx="7" cy="7" r="6" fill="var(--orange)"/><path d="M1 7h12M7 1c2.5 2.5 2.5 9.5 0 12M7 1c-2.5 2.5-2.5 9.5 0 12" fill="none" stroke="var(--slate)" stroke-width=".9"/></svg>
        <span>WWW.BEACONGUARD.COM.AU</span>
      </li>
    </ul>
  </section>

</main>
</body>
</html>
```